Asia Hotel need a card and logo

The new hotel in East Asia, Taiwan need a business card and logo design.The hotel's Chinese name is 岚柏文旅,English name is "Velmira Hotel".The core concept of this hotel is "Eco green", going to use many plant etc.,The building's first outlook draft is attached in the file for your reference.The style be modern and fashion will be good. Thank you.
Target Market(s)
East Asia
Industry/Entity Type
Hotel
Contact Information for Business Card
The hotel's name both in Chinese and English :岚柏商旅 Velmira Hotel
The logo, address, E-mail and tel number place.
Stuff's name and title.
Font styles to use
Colors
Designer to choose colors to be used in the design.
Look and feel
Each slider illustrates characteristics of the customer's brand and the style your logo design should communicate.

```html
<!DOCTYPE html>
<html lang="zh-Hant">
<head>
<meta charset="utf-8">
<title>岚柏文旅 名片</title>
<link href="https://fonts.googleapis.com/css2?family=Noto+Sans+TC:wght@400;500;700&display=swap" rel="stylesheet">
<style>
  :root {
    --backdrop: #ececec;
    --card: #ffffff;
    --ink: #8c8c8c;
    --ink-strong: #7a7a7a;
    --leaf-light: #bcd6b1;
    --leaf-deep: #a7ca9b;
  }
  html, body {
    margin: 0;
    padding: 0;
    width: 1200px;
    height: 1200px;
    overflow: hidden;
    background: var(--backdrop);
    font-family: "Noto Sans TC", sans-serif;
  }
  .business-card {
    position: absolute;
    left: 100px;
    top: 322px;
    width: 1000px;
    height: 556px;
    background: var(--card);
    overflow: hidden;
    box-shadow: 0 2px 8px rgba(0,0,0,0.08);
  }
  .leaf-corner {
    position: absolute;
    left: 0;
    top: 0;
    width: 1000px;
    height: 556px;
  }
  .text {
    position: absolute;
    left: 48px;
    margin: 0;
    color: var(--ink);
    line-height: 1;
    white-space: nowrap;
  }
  .staff-name {
    top: 120px;
    font-size: 31px;
    font-weight: 700;
    letter-spacing: 0.18em;
    color: var(--ink-strong);
  }
  .staff-title {
    top: 164px;
    font-size: 20px;
    letter-spacing: 0.2em;
  }
  .address {
    top: 236px;
    font-size: 21px;
    letter-spacing: 0.06em;
  }
  .email { top: 277px; font-size: 16px; letter-spacing: 0.08em; }
  .phone { top: 305px; font-size: 16px; letter-spacing: 0.08em; }
  .tax-id { top: 332px; font-size: 19px; letter-spacing: 0.04em; }
  .tax-id span { font-size: 16px; letter-spacing: 0.08em; }
  .website { top: 399px; font-size: 16px; letter-spacing: 0.08em; }
  .company { top: 432px; font-size: 21px; letter-spacing: 0.06em; }
</style>
</head>
<body>
  <div class="business-card">
    <svg class="leaf-corner" viewBox="0 0 1000 556" aria-hidden="true">
      <defs>
        <linearGradient id="leafFill" x1="0" y1="0" x2="1" y2="1">
          <stop offset="0" stop-color="var(--leaf-light)"/>
          <stop offset="1" stop-color="var(--leaf-deep)"/>
        </linearGradient>
      </defs>
      <path d="M631,0 C690,18 725,105 800,165 C855,208 935,214 1000,206 L1000,0 Z" fill="url(#leafFill)"/>
    </svg>

    <p class="text staff-name">林思妤</p>
    <p class="text staff-title">經理</p>

    <p class="text address">A:台中市北屯區松竹路二段86巷12號</p>
    <p class="text email">E: hi@velmirahotel.com</p>
    <p class="text phone">P: 0912-345-678</p>
    <p class="text tax-id">統編:<span>53190427</span></p>

    <p class="text website">www.velmirahotel.com</p>
    <p class="text company">岚柏開發股份有限公司</p>
  </div>
</body>
</html>
```